Around the world sailing blogger needs a book cover template designed

Hello. I'm interested in writing a series of 'guides' in relation to sailing and live-aboard cruising. Last April my husband and I sold all our possessions and purchased the largest boat we could find. Since then I've been sailing and blogging about our experiences and am slowing building up a popular website and shop. The first guide in my series is finished. It's a guide to using the VHF radio with checklist templates for the user to use. The next guide might have something to do with maintenance checklists (engine, generator, water maker, etc). Anyway, I need a cover that will act as a template for future guides so it needs to have nautical imagery, a headline, subhead, author, my logo and perhaps a quote or something and it needs to be replicated across the series. In other words it needs to be created in a way that we (or should I say you) can make more covers easily with the same look and feel. The cover needs to be created for PDF, Readly (electronic) PrintHarbor (hardcopy) at the very least... And I'll also need some thumbnails for promotional purposes. The imagery on this first one needs to cover communication/VHF radio/Sailing... I know it sounds like a boring book but it will be very useful to the user. And I really need the cover to look awesome :) To see my website it's at DriftwoodNomad.com. Final note - I've never used Pixel Forum before so this is my first time. I'm not sure if I've given you everything you need...Also, I need more than just a cover. Hopefully I can find someone that can help me with all my books and digital products that I have lined up. I'll stop typing now :)

I've just added of some pictures of our boat while we're sailing it. They might make a nice cover - I don't know. I'm really sorry for not providing this to begin with... I've never used this service before so I'm trialling it to see if it's better/easier than hirePod. I know it's really frustrating when someone wants something and doesn't give all the information up front. I just didn't understand how this all works so I apologise. I have thousands of photos...these were taken by a professional so I'm hoping they're the best... Also, keep in mind I'm looking for a series of guides and this one is on VHF radio...I can't have a photo of our boat for every guide. Next time I post a project I'll be far more knowledgable. Sorry for any inconvenience. That being said, if we do use a photo of the back of the boat, the logo is already there so we don't need the logo twice... Jo

Target Market(s)

Sailors, boaters, full time boaters...sailors sailing around the world. Anyone that owns a boat and a VHF radio. Both men and women... English speaking. Biggest audience in USA then UK, Australian, NZ, Europe..

Industry/Entity Type

Building

Font styles to use
Serif
Sans Serif

Requirements
Must have
• My logo, headlines, subhead, author line and good imagery. Using a VHF is rather boring but my book offers templates so that users can easily fill out a MAYDAY (SOS) form and feel confident when they have to broadcast the information across the radio. It an idiots guide to VHF radios...A lot of people are nervous about using them when they first start out - especially women - so this guide will help reduce anxiety.
Nice to have
• Colours that match my website might be too much blue - might be nice to have some different colors?

```html
<!DOCTYPE html>
<html lang="en">
<head>
<meta charset="utf-8">
<title>VHF Radio – A Comprehensive Beginners Guide to Sailing</title>
<link href="https://fonts.googleapis.com/css2?family=Archivo+Black&family=Cinzel:wght@600&family=Montserrat:wght@700&display=swap" rel="stylesheet">
<style>
  :root {
    --paper: #ffffff;
    --navy: #0f3e6e;
    --ink: #0a0a0a;
    --gold-light: #f7e29a;
    --gold-mid: #d4a83f;
    --gold-deep: #94691a;
  }
  html, body {
    margin: 0;
    padding: 0;
    overflow: hidden;
    background: var(--paper);
  }
  .cover {
    position: relative;
    width: 808px;
    height: 1200px;
    background: var(--paper);
    overflow: hidden;
  }
  .series-title {
    position: absolute;
    top: 24px;
    left: 0;
    width: 808px;
    margin: 0;
    text-align: center;
    font-family: "Montserrat", Arial, sans-serif;
    font-weight: 700;
    color: var(--navy);
    font-size: 30px;
    line-height: 52px;
    letter-spacing: 6px;
    text-indent: 6px;
    text-transform: uppercase;
  }
  .series-part {
    display: block;
    font-size: 24px;
    line-height: 40px;
    letter-spacing: 4px;
  }
  .brand-mark {
    position: absolute;
    top: 180px;
    left: 343px;
    width: 122px;
    height: 122px;
    border-radius: 50%;
    border: 2px solid var(--navy);
    box-sizing: border-box;
    display: flex;
    align-items: center;
    justify-content: center;
    text-align: center;
    font-family: "Montserrat", Arial, sans-serif;
    font-weight: 700;
    font-size: 14px;
    line-height: 18px;
    letter-spacing: 1px;
    color: var(--navy);
    text-transform: uppercase;
  }
  .hero-art {
    position: absolute;
    top: 275px;
    left: -330px;
    width: 690px;
    height: 690px;
    border-radius: 50%;
    background: radial-gradient(circle at 50% 50%, var(--gold-light) 0%, var(--gold-mid) 50%, var(--gold-deep) 100%);
  }
  .book-title {
    position: absolute;
    top: 496px;
    right: 46px;
    margin: 0;
    font-family: "Archivo Black", "Arial Black", sans-serif;
    font-weight: 400;
    font-size: 62px;
    line-height: 72px;
    letter-spacing: 5px;
    color: var(--ink);
    text-transform: uppercase;
  }
  .subtitle {
    position: absolute;
    top: 620px;
    right: 46px;
    margin: 0;
    text-align: right;
    font-family: "Montserrat", Arial, sans-serif;
    font-weight: 700;
    font-size: 41px;
    line-height: 45px;
    letter-spacing: 2.5px;
    color: var(--navy);
    text-transform: uppercase;
  }
  .author {
    position: absolute;
    top: 1118px;
    left: 0;
    width: 808px;
    margin: 0;
    text-align: center;
    font-family: "Cinzel", Georgia, serif;
    font-weight: 600;
    font-size: 37px;
    letter-spacing: 13px;
    text-indent: 13px;
    color: var(--navy);
    text-transform: uppercase;
  }
</style>
</head>
<body>
  <main class="cover">
    <div class="hero-art" role="img" aria-label="Golden ship's wheel with a hand holding an orange handheld VHF radio through its spokes"></div>

    <h2 class="series-title">
      A Comprehensive Beginners<br>Guide to Sailing
      <span class="series-part">Part One</span>
    </h2>

    <div class="brand-mark">Driftwood<br>Nomad</div>

    <h1 class="book-title">VHF Radio</h1>

    <p class="subtitle">Checklists<br>and<br>Templates<br>for<br>Sailors</p>

    <p class="author">Joanna Leigh Marsh</p>
  </main>
</body>
</html>
```